redesign of my existing custom website into Wordpress based website

I need someone to redesign my current website into something more classy, simplistic, modern and on trend. I would like it set up on Wordpress in a way thats easy for me to make my own additions to blogs/price changes and promotion banners. I will also need a page that is password protected so members can login and have access to all my training videos and resources.
website is www.springtidemothers.com.au

Target Market(s)

new mums

Industry/Entity Type

Fitness

Coding

Coded - Design and coding required

Number of Pages Required

5+ page

Colors
33a6d7

Requirements
Must have
• chic, modern, stylish and simplistic.
• a call to action above the page fold
• mobile friendly conversion
• a pop up message as soon as someone enters my sight offering my free report
• a members page that is password protected containing 3 youtube videos and 6 pdf attachments as resources
• a home page
• a contact us page
• an about us page
• a blog page
• a store page
Nice to have
• some examples of my peers websites that I like:
• www.norarivelle.com
• https://www.7qfx.com
• https://41bylukeharrow.com
Should not have
• anything gimmicky

```html
<!DOCTYPE html>
<html lang="en">
<head>
<meta charset="utf-8">
<title>Springtide Mothers – 12 Week Challenge</title>
<link rel="stylesheet" href="https://fonts.googleapis.com/css2?family=Open+Sans:ital,wght@0,400;0,600;0,700;0,800;1,400;1,700;1,800&display=swap">
<style>
:root{
  --pink:#e8175d;
  --pink-dark:#c9104d;
  --blue:#33a6d7;
  --ink:#2b2b2b;
  --text:#555;
  --muted:#888;
  --line:#e3e3e3;
  --white:#fff;
  --dark:#3a3a3c;
  --grey-band:#f0f0f0;
}
*{box-sizing:border-box;margin:0;padding:0}
html,body{width:1200px;height:4401px;overflow:hidden}
body{font-family:"Open Sans",Arial,sans-serif;color:var(--text);background:var(--white);position:relative}
section,header,footer{position:relative;width:1200px;overflow:hidden}
.abs{position:absolute}
.btn{position:absolute;display:flex;align-items:center;justify-content:center;gap:8px;border-radius:30px;font-weight:700;font-size:15px;letter-spacing:.5px;text-transform:uppercase;color:var(--white);background:var(--pink)}
.btn-ghost{background:transparent;border:2px solid var(--white)}

/* header */
.site-header{height:94px;background:var(--white)}
.brand{position:absolute;left:118px;top:18px;display:flex;align-items:center;gap:12px}
.brand-dot{width:56px;height:56px;border-radius:50%;border:3px solid var(--ink)}
.brand-name{font-size:20px;font-weight:700;color:var(--ink);line-height:1.1;width:120px}
.main-nav{position:absolute;left:366px;top:36px;display:flex;gap:38px;font-size:15px;font-weight:600;color:var(--ink)}
.main-nav .active{color:var(--pink)}
.btn-login{left:904px;top:30px;width:88px;height:34px;font-size:13px;color:var(--ink);background:transparent;border:1px solid var(--line)}
.btn-join{left:1006px;top:30px;width:96px;height:34px;font-size:13px}

/* hero */
.hero{height:493px;background:linear-gradient(90deg,#3b3d42 0%,#4a4c51 55%,#5b5d62 100%)}
.hero-photo{position:absolute;right:0;top:0;width:560px;height:493px;background:radial-gradient(ellipse at 60% 45%,#c9a58c 0%,#8a7a6e 35%,#55565a 75%)}
.hero-kicker{left:97px;top:100px;font-size:28px;font-weight:700;color:var(--white)}
.hero-title{left:97px;top:150px;font-size:44px;font-weight:700;line-height:1.25;color:var(--white)}
.hero-sub{left:97px;top:266px;font-size:23px;font-weight:600;color:var(--white)}
.btn-learn{left:97px;top:327px;width:164px;height:44px;font-size:14px}
.btn-hero-join{left:276px;top:327px;width:161px;height:44px;font-size:14px}

/* optin */
.optin{height:211px;background:linear-gradient(180deg,#f4f4f4,#e9e9e9)}
.optin-kicker{left:97px;top:32px;font-size:24px;font-weight:700;color:var(--pink)}
.optin-text{left:97px;top:78px;font-size:15.5px;font-weight:600;color:var(--ink)}
.optin-title{left:97px;top:112px;font-size:38px;font-weight:800;font-style:italic;color:var(--ink)}
.field{position:absolute;left:874px;width:229px;height:38px;background:var(--white);border:1px solid #d5d5d5;border-radius:3px;font-size:12px;color:var(--ink);padding:11px 14px;text-transform:uppercase}
.btn-free{left:874px;top:141px;width:229px;height:46px;font-size:15px}

/* why */
.why{height:625px}
.why-title{left:97px;top:58px;width:480px;font-size:32px;font-weight:700;line-height:1.3;color:var(--ink)}
.tick-list{position:absolute;list-style:none}
.tick-list li{display:flex;gap:14px;font-size:16px;line-height:1.5;color:var(--text);margin-bottom:18px}
.tick-list svg{flex:none;margin-top:3px}
.why-list{left:97px;top:186px;width:430px}
.video{position:absolute;left:607px;top:68px;width:494px;height:299px;background:linear-gradient(135deg,#5c5a5e,#8d7f7a 50%,#3f3f44);}
.video-bar{position:absolute;left:0;top:0;width:100%;height:34px;background:rgba(0,0,0,.55);color:var(--white);font-size:15px;padding:7px 16px}
.play{position:absolute;left:217px;top:120px}

/* cta band */
.cta-band{height:285px;background:linear-gradient(90deg,#ececec,#d9d9d9 50%,#e6e6e6)}
.cta-title{left:0;top:60px;width:1200px;text-align:center;font-size:31px;font-weight:600;color:var(--ink)}
.cta-title b{font-weight:800}
.cta-sub{left:0;top:116px;width:1200px;text-align:center;font-size:17px;color:var(--ink)}
.btn-start{left:478px;top:176px;width:226px;height:44px;font-size:14px}

/* results */
.results{height:586px;background:linear-gradient(180deg,#2d2d2f,#4a4a4c 60%,#303032)}
.results-title{left:0;top:48px;width:1200px;text-align:center;font-size:31px;font-weight:600;line-height:1.4;color:var(--white)}
.result-card{position:absolute;top:173px;width:240px;height:355px;background:var(--white);text-align:center}
.result-photo{height:173px;background:linear-gradient(135deg,#b9a294,#d8c7bb 50%,#8a7d78)}
.result-name{font-size:16px;font-weight:700;color:var(--ink);margin-top:10px}
.result-stat{font-size:17px;font-weight:700;color:var(--pink);line-height:1.3;padding:4px 14px 0}
.result-role{font-size:12px;color:var(--muted);margin-top:4px}
.result-quote{font-size:12px;line-height:1.5;color:var(--text);padding:8px 16px 0}

/* included */
.included{height:655px}
.included-photo{position:absolute;left:97px;top:71px;width:496px;height:358px;background:linear-gradient(135deg,#7a6a6e,#c7417b 45%,#4b4b55)}
.included-title{left:651px;top:78px;font-size:32px;font-weight:700;color:var(--ink)}
.inc-list{left:651px;top:140px;width:450px}
.inc-list li{margin-bottom:14px}
.price{left:651px;top:446px;font-size:24px;font-weight:700;color:var(--ink)}
.price-note{left:651px;top:488px;font-size:15px;color:var(--text)}
.btn-now{left:651px;top:534px;width:229px;height:50px;font-size:15px}

/* statement */
.statement{height:249px;background:linear-gradient(90deg,#2f2f31,#4b4b4d 50%,#2f2f31)}
.statement p{position:absolute;left:110px;top:52px;width:980px;text-align:center;font-size:30px;font-weight:600;line-height:1.45;color:var(--white)}
.statement b{font-weight:800}

/* blog */
.blog{height:558px}
.blog-title{left:0;top:52px;width:1200px;text-align:center;font-size:30px;font-weight:700;color:var(--ink)}
.post{position:absolute;top:129px;width:238px;height:370px;border:1px solid var(--line);text-align:center}
.post-photo{height:176px}
.post-title{font-size:15px;font-weight:700;color:var(--ink);line-height:1.4;padding:14px 14px 0;height:72px}
.post-excerpt{font-size:12px;line-height:1.55;color:var(--muted);padding:0 18px}
.post-meta{position:absolute;left:0;bottom:22px;width:100%;display:flex;justify-content:center;gap:22px;font-size:14px;font-weight:700;color:var(--pink)}
.post-meta span{display:flex;align-items:center;gap:6px}
.post-meta em{font-style:normal;color:var(--muted);font-weight:400;font-size:12px}

/* founder quote */
.founder{height:278px;background:var(--pink)}
.founder-photo{position:absolute;left:0;top:0;width:317px;height:278px;background:linear-gradient(135deg,#c9b3a3,#9a8d8b 55%,#6f6a6d)}
.founder-text{left:361px;top:36px;width:770px;font-size:14.5px;font-weight:700;font-style:italic;line-height:1.75;color:var(--white)}
.founder-sign{left:361px;top:200px;font-size:18px;font-weight:700;font-style:italic;color:var(--white)}

/* footer */
.site-footer{height:367px;background:var(--white)}
.foot-brand{position:absolute;left:97px;top:48px;display:flex;align-items:center;gap:10px}
.foot-brand .brand-dot{width:52px;height:52px}
.foot-brand .brand-name{font-size:18px}
.foot-h{position:absolute;top:55px;font-size:18px;font-weight:700;color:var(--ink)}
.foot-links{position:absolute;left:381px;top:98px;list-style:none;font-size:13px;line-height:2.05;color:var(--text)}
.foot-copy{left:555px;top:96px;width:290px;font-size:13px;line-height:1.6;color:var(--text)}
.foot-field{position:absolute;left:555px;width:275px;height:30px;border:1px solid #d5d5d5;font-size:12px;padding:6px 10px;color:var(--muted)}
.btn-sub{left:555px;top:238px;width:122px;height:36px;font-size:12px}
.social{position:absolute;left:892px;list-style:none;font-size:14px;color:var(--text)}
.social li{display:flex;align-items:center;gap:14px;margin-bottom:16px}
.social i{display:block;width:26px;height:26px;background:var(--blue);border-radius:4px}
.foot-rule{position:absolute;left:97px;top:297px;width:1006px;height:1px;background:var(--line)}
.copyright{left:0;top:323px;width:1200px;text-align:center;font-size:12px;color:var(--muted)}
</style>
</head>
<body>

<header class="site-header">
  <div class="brand"><span class="brand-dot"></span><span class="brand-name">Springtide Mothers</span></div>
  <nav class="main-nav">
    <span class="active">HOME</span><span>PROGRAM</span><span>BLOG</span><span>FAQ</span><span>ABOUT</span><span>CONTACT</span>
  </nav>
  <span class="btn btn-login">
    <svg width="12" height="14" viewBox="0 0 12 14"><rect x="1" y="6" width="10" height="8" rx="1" fill="#e8175d"/><path d="M3 6V4a3 3 0 0 1 6 0v2" fill="none" stroke="#e8175d" stroke-width="1.6"/></svg>LOGIN</span>
  <span class="btn btn-join">JOIN</span>
</header>

<section class="hero">
  <div class="hero-photo" role="img" aria-label="Smiling fitness coach in a green workout top against a dark studio wall"></div>
  <p class="abs hero-kicker">Transform your body and mind with the</p>
  <h1 class="abs hero-title">Springtide Mothers 12 Week<br>Challenge</h1>
  <p class="abs hero-sub">and do it all from the comfort of your own home</p>
  <span class="btn btn-learn">LEARN MORE
    <svg width="16" height="16" viewBox="0 0 16 16"><circle cx="8" cy="8" r="7" fill="none" stroke="#fff" stroke-width="1.5"/><path d="M7 5l3 3-3 3" fill="none" stroke="#fff" stroke-width="1.5"/></svg></span>
  <span class="btn btn-ghost btn-hero-join">JOIN NOW</span>
</section>

<section class="optin">
  <p class="abs optin-kicker">Bounce Back into a Fitter, Healthier, More Energetic you!</p>
  <p class="abs optin-text">Let me share with you some of my best secrets to bouncing back after baby with my FREE</p>
  <h2 class="abs optin-title">Top 10 Bouncing Back Tips</h2>
  <div class="field" style="top:38px">Name :</div>
  <div class="field" style="top:88px">Email :</div>
  <span class="btn btn-free">GET IT FREE NOW!</span>
</section>

<section class="why">
  <h2 class="abs why-title">Why choose the Springtide Mothers 12 Week Challenge</h2>
  <ul class="tick-list why-list">
    <li><svg width="18" height="18" viewBox="0 0 18 18"><circle cx="9" cy="9" r="9" fill="#e8175d"/><path d="M5 9.5l2.6 2.5L13 6.5" fill="none" stroke="#fff" stroke-width="2"/></svg>A program uniquely tailored to suit bodies post pregnancy</li>
    <li><svg width="18" height="18" viewBox="0 0 18 18"><circle cx="9" cy="9" r="9" fill="#e8175d"/><path d="M5 9.5l2.6 2.5L13 6.5" fill="none" stroke="#fff" stroke-width="2"/></svg>Options for new mums, mums who haven't done much exercise since having babies and also fitter mums</li>
    <li><svg width="18" height="18" viewBox="0 0 18 18"><circle cx="9" cy="9" r="9" fill="#e8175d"/><path d="M5 9.5l2.6 2.5L13 6.5" fill="none" stroke="#fff" stroke-width="2"/></svg>A workout program that grows with you as your fitness and strength improve</li>
    <li><svg width="18" height="18" viewBox="0 0 18 18"><circle cx="9" cy="9" r="9" fill="#e8175d"/><path d="M5 9.5l2.6 2.5L13 6.5" fill="none" stroke="#fff" stroke-width="2"/></svg>Proven training methods built by a post pregnancy specialist trainer and mum</li>
    <li><svg width="18" height="18" viewBox="0 0 18 18"><circle cx="9" cy="9" r="9" fill="#e8175d"/><path d="M5 9.5l2.6 2.5L13 6.5" fill="none" stroke="#fff" stroke-width="2"/></svg>A dedicated focus on rebuilding core strength</li>
    <li><svg width="18" height="18" viewBox="0 0 18 18"><circle cx="9" cy="9" r="9" fill="#e8175d"/><path d="M5 9.5l2.6 2.5L13 6.5" fill="none" stroke="#fff" stroke-width="2"/></svg>Delicious and healthy family friendly recipes</li>
    <li><svg width="18" height="18" viewBox="0 0 18 18"><circle cx="9" cy="9" r="9" fill="#e8175d"/><path d="M5 9.5l2.6 2.5L13 6.5" fill="none" stroke="#fff" stroke-width="2"/></svg>The ultimate convenience of being able to train from home, anytime you want!</li>
  </ul>
  <div class="video" role="img" aria-label="Video still of a mum exercising on a mat in her lounge room beside her baby">
    <div class="video-bar">Watch here to learn more</div>
    <svg class="play" width="60" height="60" viewBox="0 0 60 60"><circle cx="30" cy="30" r="30" fill="rgba(0,0,0,.6)"/><path d="M24 18l18 12-18 12z" fill="#fff"/></svg>
  </div>
</section>

<section class="cta-band">
  <p class="abs cta-title">Don't waste anymore time <b>Thinking</b> about getting back into shape</p>
  <p class="abs cta-sub">Take the first step to a fitter healthier more energetic you and join our program today!</p>
  <span class="btn btn-start">GET STARTED NOW!</span>
</section>

<section class="results">
  <h2 class="abs results-title">Check out some of the awesome results already<br>achieved by mums on our challenge</h2>
  <div class="result-card" style="left:103px">
    <div class="result-photo" role="img" aria-label="Before and after photos of a mum's progress"></div>
    <p class="result-name">Marla</p>
    <p class="result-role">Springtide Mothers Founder</p>
    <p class="result-stat">Lost 15kgs and 25cms in 12 weeks</p>
    <p class="result-quote">I used this exact program after two of my babies and lost around 15kg in just twelve weeks.</p>
  </div>
  <div class="result-card" style="left:358px">
    <div class="result-photo" role="img" aria-label="Before and after photos of a mum's progress"></div>
    <p class="result-name">Josie</p>
    <p class="result-stat">Lost 10kgs in 12 weeks</p>
    <p class="result-quote">So glad I joined, it delivers exactly what it promises and every mum should give it a go.</p>
  </div>
  <div class="result-card" style="left:613px">
    <div class="result-photo" role="img" aria-label="Before and after photos of a mum's progress"></div>
    <p class="result-name">Renata</p>
    <p class="result-stat">Lost 26cms in 12 weeks</p>
    <p class="result-quote">I am really happy with my results, I lost 26cm across my body and feel so much stronger.</p>
  </div>
  <div class="result-card" style="left:868px">
    <div class="result-photo" role="img" aria-label="Before and after photos of a mum's progress"></div>
    <p class="result-name">KT</p>
    <p class="result-stat">Lost 18cms in 12 weeks</p>
    <p class="result-quote">This program was exactly what I needed, within months I was back in my old clothes again.</p>
  </div>
</section>

<section class="included">
  <div class="included-photo" role="img" aria-label="Collage of workout videos, the healthy eating guide cover and family recipes"></div>
  <h2 class="abs included-title">What's included in the program?</h2>
  <ul class="tick-list inc-list">
    <li><svg width="18" height="18" viewBox="0 0 18 18"><circle cx="9" cy="9" r="9" fill="#e8175d"/><path d="M5 9.5l2.6 2.5L13 6.5" fill="none" stroke="#fff" stroke-width="2"/></svg>My unique 3 stage, cardio, resistance and core, 12 week training program</li>
    <li><svg width="18" height="18" viewBox="0 0 18 18"><circle cx="9" cy="9" r="9" fill="#e8175d"/><path d="M5 9.5l2.6 2.5L13 6.5" fill="none" stroke="#fff" stroke-width="2"/></svg>Full instructional online workout videos and program cards for each program</li>
    <li><svg width="18" height="18" viewBox="0 0 18 18"><circle cx="9" cy="9" r="9" fill="#e8175d"/><path d="M5 9.5l2.6 2.5L13 6.5" fill="none" stroke="#fff" stroke-width="2"/></svg>Weekly accountability charts</li>
    <li><svg width="18" height="18" viewBox="0 0 18 18"><circle cx="9" cy="9" r="9" fill="#e8175d"/><path d="M5 9.5l2.6 2.5L13 6.5" fill="none" stroke="#fff" stroke-width="2"/></svg>Weekly coaching emails</li>
    <li><svg width="18" height="18" viewBox="0 0 18 18"><circle cx="9" cy="9" r="9" fill="#e8175d"/><path d="M5 9.5l2.6 2.5L13 6.5" fill="none" stroke="#fff" stroke-width="2"/></svg>Nutritionist approved healthy eating guide</li>
    <li><svg width="18" height="18" viewBox="0 0 18 18"><circle cx="9" cy="9" r="9" fill="#e8175d"/><path d="M5 9.5l2.6 2.5L13 6.5" fill="none" stroke="#fff" stroke-width="2"/></svg>Healthy Family Favourites recipe ebook</li>
  </ul>
  <p class="abs price">All for just $89</p>
  <p class="abs price-note">One time only payment</p>
  <span class="btn btn-now">GET STARTED NOW!</span>
</section>

<section class="statement">
  <p>With 10 minutes of dedicated core exercises in each workout, I<br>will show you exactly how you can reconnect and tighten up your<br>core stomach muscles the <b>right way</b>.</p>
</section>

<section class="blog">
  <h2 class="abs blog-title">Latest Blog</h2>
  <article class="post" style="left:97px">
    <div class="post-photo" role="img" aria-label="Mum stretching in a bright lounge room" style="background:linear-gradient(135deg,#6b5a63,#b0687e 50%,#3d3d44)"></div>
    <h3 class="post-title">The benefits of training in the morning</h3>
    <p class="post-excerpt">Quick notes on easy home moves that fit around naps, school runs and busy mornings.</p>
    <div class="post-meta"><span>JAN 02</span><span><svg width="14" height="13" viewBox="0 0 14 13"><path d="M7 12.5L1.2 6.8A3.4 3.4 0 0 1 7 2.2a3.4 3.4 0 0 1 5.8 4.6z" fill="#e8175d"/></svg><em>21</em></span></div>
  </article>
  <article class="post" style="left:352px">
    <div class="post-photo" role="img" aria-label="Mum doing a floor exercise in the lounge room" style="background:linear-gradient(135deg,#4e4650,#c24a7a 50%,#3a3a40)"></div>
    <h3 class="post-title">Marla's 10 exercise lounge room cardio workout</h3>
    <p class="post-excerpt">Quick notes on easy home moves that fit around naps, school runs and busy mornings.</p>
    <div class="post-meta"><span>JAN 02</span><span><svg width="14" height="13" viewBox="0 0 14 13"><path d="M7 12.5L1.2 6.8A3.4 3.4 0 0 1 7 2.2a3.4 3.4 0 0 1 5.8 4.6z" fill="#e8175d"/></svg><em>21</em></span></div>
  </article>
  <article class="post" style="left:607px">
    <div class="post-photo" role="img" aria-label="Golden baked pastries on a plate" style="background:linear-gradient(135deg,#e9e2d6,#d7b273 50%,#b99860)"></div>
    <h3 class="post-title">Healthy Shepherds Pie Recipe</h3>
    <p class="post-excerpt">Quick notes on easy home moves that fit around naps, school runs and busy mornings.</p>
    <div class="post-meta"><span>JAN 02</span><span><svg width="14" height="13" viewBox="0 0 14 13"><path d="M7 12.5L1.2 6.8A3.4 3.4 0 0 1 7 2.2a3.4 3.4 0 0 1 5.8 4.6z" fill="#e8175d"/></svg><em>21</em></span></div>
  </article>
  <article class="post" style="left:862px">
    <div class="post-photo" role="img" aria-label="Spiced dessert with a cinnamon garnish" style="background:linear-gradient(135deg,#f0e8e0,#b86b3a 50%,#8b4a2a)"></div>
    <h3 class="post-title">Dairy, Gluten, Sugar, Guilt Free Easter the morning</h3>
    <p class="post-excerpt">Quick notes on easy home moves that fit around naps, school runs and busy mornings.</p>
    <div class="post-meta"><span>JAN 02</span><span><svg width="14" height="13" viewBox="0 0 14 13"><path d="M7 12.5L1.2 6.8A3.4 3.4 0 0 1 7 2.2a3.4 3.4 0 0 1 5.8 4.6z" fill="#e8175d"/></svg><em>21</em></span></div>
  </article>
</section>

<section class="founder">
  <div class="founder-photo" role="img" aria-label="Founder holding her baby"></div>
  <p class="abs founder-text">As a mother of 3 beautiful babies I know exactly how hard it can be to find the time and energy to focus on yourself. That's why I designed a program that was easy to follow, could fit into the life of a busy mum and was focused on all the areas that need attention after babies. I'm so passionate about sharing what I have learnt through all my post pregnancy training courses and time spent with physio's and hope I can also help you to become a fitter, healthier more energetic you!</p>
  <p class="abs founder-sign">- Marla Quinlan</p>
</section>

<footer class="site-footer">
  <div class="foot-brand"><span class="brand-dot"></span><span class="brand-name">Springtide Mothers</span></div>
  <h4 class="foot-h" style="left:381px">Quick Links</h4>
  <ul class="foot-links"><li>Home</li><li>Program</li><li>Blog</li><li>FAQ</li><li>About</li><li>Contact</li></ul>
  <h4 class="foot-h" style="left:555px">Subscribe</h4>
  <p class="abs foot-copy">Register your details below and receive loads of free information on fitness and living a healthy lifestyle</p>
  <div class="foot-field" style="top:162px">Name :</div>
  <div class="foot-field" style="top:200px">Email :</div>
  <span class="btn btn-sub">SUBSCRIBE</span>
  <h4 class="foot-h" style="left:892px">Stay Connected</h4>
  <ul class="social" style="top:100px"><li><i></i>Circlebook</li><li><i></i>Snapgram</li></ul>
  <div class="foot-rule"></div>
  <p class="abs copyright">Copyrights © 2017, Springtide Mothers. All rights reserved.</p>
</footer>

</body>
</html>
```